CalmHaven Webpage for Integrative and Holistic Psychiatric Practice

We need a webpage designed for a medical practice that focuses on integrative and holistic psychiatry. We focus on providing care to mothers and families. The name of the company is Calm Haven, incorporated, A Professional Medical Corporation.

We'd like the color palette to be earthy/natural with the same look and feel as our logo that's attached. We're not set on anything, so feel free to have fun with the palette. We just want it to be warm and inviting in particular for Moms!

We'd like to have our logo in the top left with links below it either centered or to the right. We really like websites like http://www.brightmeadowclinic.example/home.html and http://www.tarnwickmindpartners.example/site/ to give you an idea of what we're looking for.

For links, we're looking for the following. Dummy text is fine, we're still getting content together:

* Home
* About Us - this page would have headings for Directions, Staff, Appointment Scheduling
* Services Provided - headings for 8 different services
* Patient Resources - headings for Patient Forms, Fees, Articles
* FAQ
* Contact Us

The webpage will be hosted as an Office 365 Public Website, so feel free to use whatever SharePoint integration you would like, but it's not necessary.

Thank you!

```html
<!DOCTYPE html>
<html lang="en">
<head>
<meta charset="utf-8">
<title>CalmHaven – Integrative and Holistic Psychiatry</title>
<link href="https://fonts.googleapis.com/css2?family=Open+Sans:wght@400;600;700&family=PT+Sans+Narrow&display=swap" rel="stylesheet">
<style>
:root{
  --green:#2f6b07;
  --green-dark:#1f4d03;
  --green-light:#8fd14f;
  --ink:#3a3a3a;
  --muted:#666;
  --rule:#cfcfcf;
  --gray:#cfcfcf;
  --brown:#6b3a12;
  --white:#fff;
  --black:#000;
}
*{box-sizing:border-box;margin:0;padding:0}
html,body{width:889px;height:1200px;overflow:hidden;background:var(--white)}
body{font-family:"Open Sans",sans-serif;color:var(--ink);position:relative}
.topbar{height:64px;position:relative}
.contact-list{position:absolute;right:73px;top:9px;display:flex;gap:24px;font-size:17.5px;color:var(--muted);list-style:none;white-space:nowrap}
.contact-list li{display:flex;align-items:center;gap:5px}
.contact-list svg{fill:var(--green)}
.navbar{height:31px;background:var(--green);position:relative}
.nav{list-style:none;font-size:11.6px;color:var(--white);white-space:nowrap}
.nav li{position:absolute;top:4px;height:23px;line-height:23px}
.nav li.active{background:var(--green-dark);border-radius:2px;width:59px;text-align:center}
.brand-box{position:absolute;left:74px;top:0;width:190px;height:130px;background:var(--white);box-shadow:0 2px 6px rgba(0,0,0,.3);z-index:2;display:flex;align-items:center;justify-content:center;gap:8px}
.brand-mark{width:22px;height:22px;border-radius:50%;background:var(--green)}
.brand-name{font-size:20px;font-weight:600;color:var(--brown)}
.hero{height:214px;position:relative;background:linear-gradient(#5c86b4 0%,#9bb8d2 45%,#b9cfdc 60%,#6f9b32 72%,#3c6a17 100%);text-align:center;color:var(--white)}
.hero h1{position:absolute;top:70px;width:100%;font-size:30px;font-weight:700;letter-spacing:.5px;text-shadow:0 1px 3px rgba(0,0,0,.4)}
.hero p{position:absolute;top:111px;width:100%;font-size:23px;text-shadow:0 1px 3px rgba(0,0,0,.4)}
.dots{position:absolute;top:182px;left:405px;display:flex;gap:4px}
.dots span{width:10px;height:10px;border:1.5px solid var(--white);border-radius:50%}
.dots span.on{background:var(--white)}
.intro{height:244px;position:relative}
.section-title{font-size:16px;font-weight:600;color:#555;padding-bottom:6px;border-bottom:2px solid var(--rule)}
.about{position:absolute;left:74px;top:13px;width:488px}
.about p{font-size:8.8px;line-height:15.2px;color:var(--muted);margin-top:10px;text-align:justify;letter-spacing:-.05px}
.about p:first-of-type{margin-top:14px}
.read-more{position:absolute;top:218px;font-size:8px;color:var(--brown);font-weight:600}
.specialties{position:absolute;left:581px;top:13px;width:234px}
.specialties ul{list-style:none;margin-top:13px;font-size:8.8px;line-height:15.3px;color:var(--muted);width:242px;white-space:nowrap}
.specialties li::before{content:"›";margin-right:12px;color:#888}
.features{height:318px;background:var(--green);position:relative;color:var(--white)}
.feature{position:absolute;top:20px;width:220px;text-align:center}
.feature .photo{width:164px;height:164px;border-radius:50%;margin:0 auto;border:3px solid #e8e8e8;box-shadow:0 0 0 1px var(--green),0 0 0 3px #bbb}
.feature h3{font-family:"PT Sans Narrow",sans-serif;font-weight:400;font-size:15px;margin-top:25px}
.feature p{font-size:8.8px;line-height:15.2px;margin-top:10px}
.divider{position:absolute;top:22px;width:1px;height:212px;background:#5f8f3a}
.lower{height:269px;background:var(--gray);position:relative}
.lower h2{font-size:19px;font-weight:400;color:var(--green-dark)}
.arrows{position:absolute;display:flex;gap:10px}
.arrows span{width:19px;height:19px;background:var(--green);display:flex;align-items:center;justify-content:center}
.arrows svg{stroke:var(--white);fill:none;stroke-width:2}
.blog{position:absolute;left:73px;top:15px;width:363px}
.posts{display:flex;gap:18px;margin-top:10px}
.post{width:172px}
.post .thumb{height:94px;background:linear-gradient(#4f86c9 0%,#bcd3ea 55%,#e9f0f5 80%,#4c8f1a 92%)}
.post h4{font-size:9.2px;font-weight:400;color:#222;margin-top:10px;white-space:nowrap}
.post .date{font-size:7px;color:var(--green);margin-top:3px}
.post p{font-size:8.8px;line-height:15.2px;color:var(--muted);margin-top:8px}
.testimonials{position:absolute;left:453px;top:15px;width:363px}
.testi-box{margin-top:9px;height:210px;background:var(--green);border:2px solid #eee;padding:19px 16px 0 22px}
.testimonial{display:flex;gap:20px;height:95px}
.testimonial .avatar{width:82px;height:82px;border-radius:50%;flex:none;background:radial-gradient(circle at 50% 40%,#e8c9a8,#b58c62 60%,#dcdcdc 62%);border:2px solid #eee}
.testimonial p{font-size:8.8px;line-height:15.2px;color:var(--white);margin-top:15px}
.testimonial cite{display:block;font-style:normal;color:var(--green-light);font-size:12px;margin-top:4px}
.footer{height:60px;background:var(--black);position:relative}
.footer small{position:absolute;left:73px;top:26px;font-size:7.5px;color:var(--white);font-weight:600}
.social{position:absolute;right:72px;top:16px;display:flex;gap:8px;list-style:none}
.social li{width:27px;height:27px;border-radius:50%;background:var(--white)}
</style>
</head>
<body>
<header class="topbar">
  <ul class="contact-list">
    <li><svg width="18" height="14" viewBox="0 0 20 15"><path d="M0 0h20v15H0z M1 1l9 7 9-7" stroke="#fff" stroke-width="1.5"/></svg>hello@calmhaven.example</li>
    <li><svg width="19" height="15" viewBox="0 0 20 16"><ellipse cx="10" cy="7" rx="10" ry="7"/><path d="M3 11l-2 5 6-3z"/></svg>Live Chat</li>
    <li><svg width="15" height="15" viewBox="0 0 16 16"><path d="M3 0l3 4-2 2c1 2 3 4 6 6l2-2 4 3-2 3C7 16 0 9 0 3z"/></svg>555-014-2290</li>
  </ul>
</header>
<div class="brand-box"><span class="brand-mark"></span><span class="brand-name">CalmHaven</span></div>
<nav class="navbar">
  <ul class="nav">
    <li class="active" style="left:313px">Home</li>
    <li style="left:385px">Integrative Services</li>
    <li style="left:510px">About</li>
    <li style="left:568px">Rates &amp; Insurance</li>
    <li style="left:679px">Patient Portal</li>
    <li style="left:775px">Contact</li>
  </ul>
</nav>
<section class="hero" role="img" aria-label="Photo of a lone tree on a green meadow under a blue sky">
  <h1>WELCOME</h1>
  <p>INTEGRATIVE AND HOLISTIC PSYCHIATRY</p>
  <div class="dots"><span class="on"></span><span></span><span></span><span></span></div>
</section>
<section class="intro">
  <div class="about">
    <h2 class="section-title">About us</h2>
    <p>Lorem ipsum dolor sit amet, consectetuer adipiscing elit, sed diam nonummy nibh euismod tincidunt ut laoreet dolore magna aliquam erat volutpat. Ut wisi enim ad minim veniam, Lorem ipsum dolor sit amet, consectetuer adipiscing elit, sed diam nonummy nibh euismod tincidunt ut laoreet dolore magna aliquam erat volutpat. Ut wisi enim ad minim veniam, Lorem ipsum dolor sit amet, consectetuer adipiscing elit, sed diam nonummy</p>
    <p>Lorem ipsum dolor sit amet, consectetuer adipiscing elit, sed diam nonummy nibh euismod tincidunt ut laoreet dolore magna aliquam erat volutpat. Ut wisi enim ad minim veniam, Lorem ipsum dolor sit amet, consectetuer adipiscing elit, sed diam nonummy nibh euismod tincidunt ut laoreet dolore magna aliquam erat volutpat. Ut wisi enim ad minim veniam, Lorem ipsum dolor sit amet, consectetuer adipiscing elit, sed diam nonummy</p>
  </div>
  <a class="read-more" style="left:73px">READ MORE</a>
  <div class="specialties">
    <h2 class="section-title">Specialties</h2>
    <ul>
      <li>Lorem ipsum</li><li>dolor sit amet,</li><li>consectetuer</li><li>adipiscing elit,</li><li>sed diam nonummy</li><li>nibh euismod tincidunt ut laoreet dolore magna</li><li>aliquam erat v</li><li>olutpat. Ut wisi e</li><li>nim ad minim v</li><li>eniam, Lorem</li>
    </ul>
  </div>
  <a class="read-more" style="left:586px">READ MORE</a>
</section>
<section class="features">
  <div class="feature" style="left:72px"><div class="photo" role="img" aria-label="Photo of a smiling mother holding her baby" style="background:radial-gradient(circle at 40% 45%,#f1d2bd,#c9a48c 55%,#efe9e4 80%)"></div><h3 style="margin-top:32px">adipiscing elit, s</h3><p>Lorem ipsum dolor sit amet,<br>consectetuer adipiscing elit, sed diam<br>nonummy nibh euismod tincidunt ut<br>ad minim veniam,</p></div>
  <div class="divider" style="left:316px"></div>
  <div class="feature" style="left:326px"><div class="photo" role="img" aria-label="Photo of a tired young woman resting her head on her hand" style="background:radial-gradient(circle at 45% 40%,#e0b9a3,#a65f4e 55%,#7a4a42 85%)"></div><h3>adipiscing elit, s</h3><p>Lorem ipsum dolor sit amet,<br>consectetuer adipiscing elit, sed diam<br>nonummy nibh euismod tincidunt ut<br>ad minim veniam,</p></div>
  <div class="divider" style="left:571px"></div>
  <div class="feature" style="left:583px"><div class="photo" role="img" aria-label="Photo of a happy woman looking upward" style="background:radial-gradient(circle at 50% 40%,#eac9b3,#6b4636 50%,#f4f4f4 75%)"></div><h3>adipiscing elit, s</h3><p>Lorem ipsum dolor sit amet,<br>consectetuer adipiscing elit, sed diam<br>nonummy nibh euismod tincidunt ut<br>ad minim veniam,</p></div>
</section>
<section class="lower">
  <div class="blog">
    <h2>Recent Blog</h2>
    <div class="arrows" style="left:313px;top:3px"><span><svg width="8" height="10"><path d="M6 1L2 5l4 4"/></svg></span><span><svg width="8" height="10"><path d="M2 1l4 4-4 4"/></svg></span></div>
    <div class="posts">
      <article class="post"><div class="thumb" role="img" aria-label="Photo of a tree on a hill under a blue sky"></div><h4>Lorem ipsum dolor sit amet, sit amet,</h4><div class="date">▣ 13 OCT 2014</div><p>Lorem ipsum dolor sit amet, consectetuer adipiscing elit, sed diam nonummy nibh euismod tincidunt ut ad minim veniam,</p></article>
      <article class="post"><div class="thumb" role="img" aria-label="Photo of a tree on a hill under a blue sky"></div><h4>Lorem ipsum dolor sit amet, sit amet,</h4><div class="date">▣ 13 OCT 2014</div><p>Lorem ipsum dolor sit amet, consectetuer adipiscing elit, sed diam nonummy nibh euismod tincidunt ut ad minim veniam,</p></article>
    </div>
  </div>
  <div class="testimonials">
    <h2>Testimonials</h2>
    <div class="arrows" style="left:314px;top:3px"><span><svg width="8" height="10"><path d="M6 1L2 5l4 4"/></svg></span><span><svg width="8" height="10"><path d="M2 1l4 4-4 4"/></svg></span></div>
    <div class="testi-box">
      <div class="testimonial"><div class="avatar" role="img" aria-label="Portrait photo of a smiling client"></div><div><p>Lorem ipsum dolor sit amet, consectetuer adipiscing elit, sed diam nonummy nibh euismod tincidunt ut ad minim veniam,</p><cite>nora vell</cite></div></div>
      <div class="testimonial"><div class="avatar" role="img" aria-label="Portrait photo of a smiling client"></div><div><p>Lorem ipsum dolor sit amet, consectetuer adipiscing elit, sed diam nonummy nibh euismod tincidunt ut ad minim veniam,</p><cite>nora vell</cite></div></div>
    </div>
  </div>
</section>
<footer class="footer">
  <small>Copyright 2014. All rights reserved.</small>
  <ul class="social" aria-label="Social links"><li></li><li></li><li></li><li></li></ul>
</footer>
</body>
</html>
```